Falverino’s Artisan Pizzeria Menu Contest

I’m looking for a menu design for a new pizzeria - it’s farm to table type of restaurant - more upscale than a typical pizzeria - white washed wood interior with some industrial accents - I am looking for a creative menu layout using the attached sample menu items -
Falverino’s is an artisanal pizzeria with an atmosphere that will make you feel at home for any situation, first date, anniversary, business lunch, boys night out or girls night out with a menu inspired by the idea of a simple honest cooking paired with fresh – quality ingredients. Full service dining experience that is still casual but dedicated to extraordinary hospitality.
While developing the menu we have created a network of amazing farms and purveyors to supply our restaurant with fresh milled 100% California flour for our hand crafted dough, as well as sustainably farmed organic produce, meats and cheeses.
The menu includes classics like the Margherita pizza to daily seasonal specials, fresh salads to rustic small plates including moms meatball recipe to a fresh local burrata with handmade bread. Each dish reflects our passion for sourcing the freshest quality local ingredients.
To compliment the menu, Falverino’s serves an extensive wine list with selections focusing on Italian varietals. The cocktail program has been carefully crafted to offer something to entice ever palate and the beer list has unique selections of the world’s finest brewers.
Target Market(s)
25-45 year old men and women
Industry/Entity Type
American Restaurant
Requirements
Must have
- professional tone
Nice to have
- a balance of elegance and industrial (rustic)
Should not have
- photos or playful graphics etc..

```html
<!DOCTYPE html>
<html lang="en">
<head>
<meta charset="utf-8">
<title>Falverino’s Artisan Pizzeria Menu</title>
<link rel="stylesheet" href="https://fonts.googleapis.com/css2?family=Montserrat:wght@600;700&family=Yellowtail&family=Crimson+Text:wght@400&display=swap">
<style>
  :root{
    --canvas:#eeeeee;
    --paper:#dedede;
    --paper-light:#e6e6e6;
    --ink:#1c1c1c;
    --accent:#e8444f;
    --band:#b9b9b9;
    --badge:#1a1a1a;
  }
  *{box-sizing:border-box;margin:0;padding:0}
  html,body{width:1200px;height:1200px;overflow:hidden;background:var(--canvas)}
  .menu{
    position:absolute;left:174px;top:0;width:851px;height:1200px;
    background:linear-gradient(160deg,var(--paper-light),var(--paper));
    color:var(--ink);
  }
  .section{position:absolute}
  .section-title{position:relative;height:56px;margin-bottom:6px}
  .section-title .band{position:absolute;left:0;top:4px;width:172px;height:44px;background:var(--band);opacity:.55;border-radius:6px 18px 8px 20px}
  .section-title h2{
    position:relative;font-family:"Yellowtail","Brush Script MT",cursive;font-weight:400;
    font-size:44px;line-height:52px;color:var(--accent);padding-left:16px;white-space:nowrap;
  }
  .item{margin-bottom:11px}
  .row{display:flex;align-items:baseline;font-family:"Montserrat",sans-serif;font-weight:700}
  .name{font-size:15px;white-space:nowrap}
  .leader{flex:1;margin:0 4px;height:2px;align-self:center;
    background:repeating-linear-gradient(90deg,var(--ink) 0 5px,transparent 5px 9px);transform:translateY(3px)}
  .price{font-size:20px;color:var(--accent);line-height:18px;white-space:nowrap}
  .desc{font-family:"Crimson Text",serif;font-size:11px;line-height:14px;margin-top:1px;white-space:nowrap}
  .col-left{left:66px;width:292px}
  .col-right{left:469px;width:285px}
  .dips{display:grid;grid-template-columns:153px 150px;column-gap:22px;row-gap:6px}
  .brand{
    position:absolute;left:52px;top:1095px;display:flex;align-items:center;gap:10px;
    font-family:"Montserrat",sans-serif;font-weight:700;font-size:30px;color:var(--badge);letter-spacing:1px
  }
  .brand .mark{width:14px;height:14px;background:var(--badge)}
</style>
</head>
<body>
<main class="menu">

  <section class="section col-left" style="top:52px">
    <div class="section-title"><div class="band" role="img" aria-label="grey brush stroke behind heading"></div><h2>Appetizers</h2></div>
    <div class="item"><div class="row"><span class="name">Brussels</span><span class="leader"></span><span class="price">$10</span></div><p class="desc">pan seared brussel sprouts with a drizzle of balsamic reduction<br>and parm and bread crumbs</p></div>
    <div class="item"><div class="row"><span class="name">Meatballs</span><span class="leader"></span><span class="price">$13</span></div><p class="desc">moms meatballs handmade secret recipe for over 75 years</p></div>
    <div class="item"><div class="row"><span class="name">Mussels</span><span class="leader"></span><span class="price">$15</span></div><p class="desc">New Zealand Mussels in a tomato broth</p></div>
    <div class="item"><div class="row"><span class="name">Romanesco</span><span class="leader"></span><span class="price">$11</span></div><p class="desc">flash fried romanesco served atop a spicy aioli</p></div>
    <div class="item"><div class="row"><span class="name">Chicken wings</span><span class="leader"></span><span class="price">$10</span></div><p class="desc">italian fried chicken wings with a kick</p></div>
    <div class="item"><div class="row"><span class="name">Burrata</span><span class="leader"></span><span class="price">$13</span></div><p class="desc">Local burrata served with apples grapes and fresh made bread</p></div>
  </section>

  <section class="section col-left" style="top:434px;width:305px">
    <div class="section-title"><div class="band" role="img" aria-label="grey brush stroke behind heading"></div><h2>Salads</h2></div>
    <div class="item"><div class="row"><span class="name">Chopped Salad</span><span class="leader"></span><span class="price">$13</span></div><p class="desc">Lettuce mix with tomato, onions, peppers, pepperoni, chick peas,<br>fresh mozz, italian herb ving</p></div>
    <div class="item"><div class="row"><span class="name">Caesar Salad</span><span class="leader"></span><span class="price">$11</span></div><p class="desc">traditional caesar salad rich and creamy extra shaved parmesan</p></div>
    <div class="item"><div class="row"><span class="name">Farm Salad</span><span class="leader"></span><span class="price">$15</span></div><p class="desc">seasonal farmers market salad</p></div>
    <div class="item"><div class="row"><span class="name">Grilled Little Gem</span><span class="leader"></span><span class="price">$11</span></div><p class="desc">Grilled little gems with bacon, tomato, red onions<br>and blue cheese dressing</p></div>
    <div class="item"><div class="row"><span class="name">Spinach and Arugula Salad</span><span class="leader"></span><span class="price">$12</span></div><p class="desc">Spinach and argula, red pepperstossed in a lemon ving<br>and housemade croutons</p></div>
  </section>

  <section class="section col-left" style="top:792px;width:305px">
    <div class="section-title"><div class="band" role="img" aria-label="grey brush stroke behind heading" style="width:185px"></div><h2>Daily Soup</h2></div>
    <div class="item"><div class="row"><span class="name">Tomato bisque</span><span class="leader"></span><span class="price">$8</span></div></div>
  </section>

  <section class="section" style="top:906px;left:61px">
    <div class="section-title"><div class="band" role="img" aria-label="grey brush stroke behind heading"></div><h2 style="padding-left:40px">Dips</h2></div>
    <div class="dips">
      <div class="row"><span class="name">ranch</span><span class="leader"></span><span class="price">$1</span></div>
      <div class="row"><span class="name">spicy dip</span><span class="leader"></span><span class="price">$1</span></div>
      <div class="row"><span class="name">tomato sauce</span><span class="leader"></span><span class="price">$1</span></div>
      <div class="row"><span class="name">blue cheese</span><span class="leader"></span><span class="price">$1</span></div>
    </div>
  </section>

  <div class="brand"><span class="mark"></span>FALVERINO’S</div>

  <section class="section col-right" style="top:52px">
    <div class="section-title"><div class="band" role="img" aria-label="grey brush stroke behind heading"></div><h2>Sandwiches</h2></div>
    <div style="height:6px"></div>
    <div class="item"><div class="row"><span class="name">Italian sub</span><span class="leader"></span><span class="price">$13</span></div><p class="desc">Prociutto, salumi, turkey, provolone, lettuce, tomato and herb aioli with<br>spicy gardenia</p></div>
    <div class="item"><div class="row"><span class="name">Turkey sandwich</span><span class="leader"></span><span class="price">$12</span></div><p class="desc">housemade bread - turkey, cheddar cheese, butter lettuce, tomato<br>and mustard aioli</p></div>
    <div class="item"><div class="row"><span class="name">Meatball sub</span><span class="leader"></span><span class="price">$13</span></div><p class="desc">Moms meatballs melted provolone on a housemade roll</p></div>
    <div class="item"><div class="row"><span class="name">Plantwise burger</span><span class="leader"></span><span class="price">$14</span></div><p class="desc">Housemade bun - arugula , tomato, onion<br>and a sundried tomato spread</p></div>
    <div class="item"><div class="row"><span class="name">Chicken sandwich</span><span class="leader"></span><span class="price">$13</span></div><p class="desc">Fried chicken or chicken breast, provolone, argula, tomato,<br>served with a spicy aioli</p></div>
  </section>

  <section class="section col-right" style="top:434px">
    <div class="section-title"><div class="band" role="img" aria-label="grey brush stroke behind heading"></div><h2>Pizzas</h2></div>
    <div class="item"><div class="row"><span class="name">Margherita</span><span class="leader"></span><span class="price">$14</span></div><p class="desc">Classic Margherita pizza - Fresh Mozz Tomato Sauce and Basil</p></div>
    <div class="item"><div class="row"><span class="name">Organic Sausage</span><span class="leader"></span><span class="price">$16</span></div><p class="desc">Organic Sausage Housemade Red Sauce Mozz hint of fennel</p></div>
    <div class="item"><div class="row"><span class="name">Pepperoni</span><span class="leader"></span><span class="price">$16</span></div><p class="desc">Dalton Pepperoni - Housemade Red Sauce Chile flakes and Mozz</p></div>
    <div class="item"><div class="row"><span class="name">Salumi and Burrata</span><span class="leader"></span><span class="price">$17</span></div><p class="desc">Salumi dried Red Sauce finished with whipped burrata</p></div>
    <div class="item" style="margin-bottom:6px"><div class="row"><span class="name">Daily special</span><span class="leader"></span><span class="price">$17</span></div></div>
    <div class="item"><div class="row"><span class="name">Mushroom</span><span class="leader"></span><span class="price">$15</span></div><p class="desc">Shaved mushrooms with a Parmesan cream and melted onions</p></div>
    <div class="item"><div class="row"><span class="name">Prosciutto and egg</span><span class="leader"></span><span class="price">$16</span></div><p class="desc">Parma Prosciutto Parmesan cream with Holmsberg<br>and gruyere finished with an organic egg</p></div>
    <div class="item"><div class="row"><span class="name">Quarttro Formaggi</span><span class="leader"></span><span class="price">$15</span></div><p class="desc">Four cheese combination - mozz - fontina - parm cream<br>and gruyere chile flakes and oregano</p></div>
    <div class="item"><div class="row"><span class="name">Farmers Pizza</span><span class="leader"></span><span class="price">$17</span></div><p class="desc">Seasonal vegatables cream sauce and a variety of cheese</p></div>
    <div class="item"><div class="row"><span class="name">Keto friendly</span><span class="leader"></span><span class="price">$17</span></div><p class="desc">Cauliflower crust, spinach and kale , parm cream sauce</p></div>
  </section>

  <section class="section" style="top:980px;left:461px;width:255px">
    <div class="section-title"><div class="band" role="img" aria-label="grey brush stroke behind heading"></div><h2 style="padding-left:36px">Crusts</h2></div>
    <div class="item"><div class="row"><span class="name">traditional</span></div><p class="desc">orginal crust you can’t miss</p></div>
    <div class="item"><div class="row"><span class="name">Gluten free</span><span class="leader"></span><span class="price">$3</span></div><p class="desc">orginal crust you can’t miss</p></div>
    <div class="item"><div class="row"><span class="name">Cauliflower</span><span class="leader"></span><span class="price">$3</span></div><p class="desc">Vegans have needs</p></div>
  </section>

</main>
</body>
</html>
```